Larkmoor Capital - Financial Planning Solutions

Larkmoor Capital is a financial planning business in Melbourne, Australia. We cater to all kinds of clients from high net worth individuals to young people just starting a career. We need a chart, which will be included in client pitches, presentations and on our website, that conveys the various areas that we are able to provide client solutions.
We have attached three rudimentary interpretations of what we're talking about, one of which includes our logo. With each area of advice we have included a brief description of what it is. The different areas are not necessarily linked, so it's not a circular process but there is a logical progression to them: clients can ask us to get involved with any of the steps.
We are pretty open to suggestions as to the best presentation but are quite interested in an infographics approach.
You can check out our website at www.larkmoorcapital.com.au to see a bit about us, but please be aware that we are changing our investment philosophy and the tone of the website to a broader appeal.
Cheers, Oliver

```html
<!DOCTYPE html>
<html lang="en">
<head>
<meta charset="utf-8">
<title>Larkmoor Capital – Financial Planning Solutions</title>
<link rel="stylesheet" href="https://fonts.googleapis.com/css2?family=Montserrat:wght@300;400;600;700&display=swap">
<style>
  :root {
    --frame: #5f5f61;
    --slide: #ebebeb;
    --band: #2a2a2a;
    --white: #ffffff;
    --ink: #333335;
    --node: #59595b;
    --gold: #a38f5e;
    --gold-soft: #cbbc8f;
    --footer-text: #c9c9c9;
  }
  html, body {
    margin: 0;
    padding: 0;
    width: 798px;
    height: 1200px;
    overflow: hidden;
    background: var(--frame);
  }
  .artboard { display: block; width: 798px; height: 1200px; }
  .frame-bg { fill: var(--frame); }
  .slide-bg { fill: var(--slide); }
  .dark-band { fill: var(--band); }
  .title-band { fill: var(--white); }
  .band-mark { fill: #e6e6e6; }
  .brand-mark { fill: var(--ink); }
  .brand-name {
    font-family: "Montserrat", sans-serif;
    font-weight: 400;
    fill: var(--ink);
  }
  .tagline {
    font-family: "Montserrat", sans-serif;
    font-weight: 300;
    font-size: 30px;
    fill: var(--gold);
  }
  .slide-title {
    font-family: "Montserrat", sans-serif;
    font-weight: 400;
    font-size: 18px;
    fill: var(--gold);
  }
  .tab { fill: var(--gold); }
  .ring { fill: none; stroke: var(--gold-soft); stroke-width: 1.6; }
  .spoke { stroke: var(--gold-soft); stroke-width: 1.3; stroke-dasharray: 3 3; }
  .pointer { stroke: var(--gold-soft); stroke-width: 1.3; stroke-dasharray: 3 3; fill: none; }
  .pointer-head { fill: var(--gold-soft); }
  .hub { fill: var(--node); }
  .hub-name {
    font-family: "Montserrat", sans-serif;
    font-weight: 600;
    font-size: 11px;
    fill: #e8e8e8;
    text-anchor: middle;
  }
  .node { fill: var(--node); }
  .node-label {
    font-family: "Montserrat", sans-serif;
    font-weight: 700;
    font-size: 10px;
    fill: var(--white);
    text-anchor: middle;
  }
  .note {
    font-family: "Montserrat", sans-serif;
    font-weight: 400;
    font-size: 13px;
    fill: var(--gold);
  }
  .note-right { text-anchor: end; }
  .footer-text {
    font-family: "Montserrat", sans-serif;
    font-weight: 400;
    font-size: 11px;
    fill: var(--footer-text);
  }
</style>
</head>
<body>
<svg class="artboard" viewBox="0 0 822 1236" xmlns="http://www.w3.org/2000/svg">
  <rect class="frame-bg" x="0" y="0" width="822" height="1236"/>

  <!-- Cover slide -->
  <g class="cover-slide">
    <rect class="slide-bg" x="19" y="21" width="782" height="585"/>
    <rect class="dark-band" x="19" y="21" width="782" height="28"/>
    <rect class="band-mark" x="403" y="26" width="14" height="14"/>

    <rect class="brand-mark" x="380" y="180" width="60" height="60"/>
    <text class="brand-name" x="410" y="313" font-size="48" text-anchor="middle" textLength="330" lengthAdjust="spacing">LARKMOOR</text>
    <text class="brand-name" x="410" y="352" font-size="24" text-anchor="middle" textLength="190" lengthAdjust="spacing">CAPITAL</text>

    <text class="tagline" x="410" y="506" text-anchor="middle">Financial Planning Solutions</text>
  </g>

  <!-- Services slide -->
  <g class="services-slide">
    <rect class="slide-bg" x="19" y="626" width="782" height="585"/>
    <rect class="title-band" x="19" y="626" width="782" height="36"/>
    <rect class="tab" x="33" y="626" width="16" height="32"/>
    <text class="slide-title" x="60" y="651">Larkmoor Capital Is Able To Help At Any Stage</text>

    <g class="service-wheel">
      <circle class="ring" cx="410" cy="912" r="136"/>

      <g class="spokes">
        <line class="spoke" x1="410" y1="850" x2="410" y2="824"/>
        <line class="spoke" x1="454" y1="868" x2="485" y2="840"/>
        <line class="spoke" x1="472" y1="912" x2="507" y2="912"/>
        <line class="spoke" x1="454" y1="956" x2="485" y2="985"/>
        <line class="spoke" x1="410" y1="974" x2="410" y2="1009"/>
        <line class="spoke" x1="366" y1="956" x2="334" y2="985"/>
        <line class="spoke" x1="348" y1="912" x2="314" y2="912"/>
        <line class="spoke" x1="366" y1="868" x2="334" y2="840"/>
      </g>

      <circle class="ring" cx="410" cy="912" r="62"/>
      <circle class="hub" cx="410" cy="912" r="55"/>
      <text class="hub-name" x="410" y="909">Larkmoor</text>
      <text class="hub-name" x="410" y="923">Capital</text>

      <g class="nodes">
        <circle class="node" cx="410" cy="784" r="40"/>
        <text class="node-label" x="410" y="780">Income</text>
        <text class="node-label" x="410" y="791">Generated</text>

        <circle class="node" cx="513" cy="820" r="40"/>
        <text class="node-label" x="513" y="824">Tax Advice</text>

        <circle class="node" cx="547" cy="911" r="40"/>
        <text class="node-label" x="547" y="908">Financial</text>
        <text class="node-label" x="547" y="919">Planning</text>

        <circle class="node" cx="513" cy="1013" r="40"/>
        <text class="node-label" x="513" y="1017">Debt</text>

        <circle class="node" cx="409" cy="1049" r="40"/>
        <text class="node-label" x="409" y="1053">Superannuation</text>

        <circle class="node" cx="305" cy="1013" r="40"/>
        <text class="node-label" x="305" y="1015">Investment</text>
        <text class="node-label" x="305" y="1026">Portfolio</text>

        <circle class="node" cx="274" cy="911" r="40"/>
        <text class="node-label" x="274" y="915">Insurance</text>

        <circle class="node" cx="306" cy="820" r="40"/>
        <text class="node-label" x="306" y="816">Estate</text>
        <text class="node-label" x="306" y="827">Planning</text>
      </g>

      <g class="pointers">
        <line class="pointer" x1="410" y1="743" x2="410" y2="722"/>
        <path class="pointer-head" d="M406 722 L410 714 L414 722 Z"/>

        <line class="pointer" x1="541" y1="791" x2="550" y2="782"/>
        <path class="pointer-head" d="M547 780 L556 776 L553 785 Z"/>

        <line class="pointer" x1="588" y1="911" x2="599" y2="911"/>
        <path class="pointer-head" d="M599 907 L607 911 L599 915 Z"/>

        <line class="pointer" x1="541" y1="1041" x2="551" y2="1051"/>
        <path class="pointer-head" d="M548 1053 L557 1057 L553 1048 Z"/>

        <line class="pointer" x1="409" y1="1090" x2="409" y2="1106"/>
        <path class="pointer-head" d="M405 1106 L409 1114 L413 1106 Z"/>

        <line class="pointer" x1="277" y1="1041" x2="268" y2="1050"/>
        <path class="pointer-head" d="M266 1047 L261 1056 L271 1053 Z"/>

        <line class="pointer" x1="233" y1="911" x2="219" y2="911"/>
        <path class="pointer-head" d="M219 907 L211 911 L219 915 Z"/>

        <line class="pointer" x1="277" y1="792" x2="268" y2="785"/>
        <path class="pointer-head" d="M271 782 L261 779 L266 788 Z"/>
      </g>

      <g class="notes">
        <rect class="tab" x="384" y="690" width="16" height="37"/>
        <text class="note" x="405" y="702">Funds earned from work</text>
        <text class="note" x="405" y="715">or investments</text>

        <rect class="tab" x="562" y="757" width="16" height="38"/>
        <text class="note" x="583" y="769">Maximize after</text>
        <text class="note" x="583" y="782">tax income</text>

        <rect class="tab" x="612" y="892" width="16" height="38"/>
        <text class="note" x="633" y="903">An application</text>
        <text class="note" x="633" y="916">roadmap of your</text>
        <text class="note" x="633" y="929">after tax income</text>

        <rect class="tab" x="565" y="1048" width="16" height="37"/>
        <text class="note" x="586" y="1060">To fund the</text>
        <text class="note" x="586" y="1073">purchase of a house</text>
        <text class="note" x="586" y="1086">or other asset</text>

        <rect class="tab" x="401" y="1118" width="16" height="38"/>
        <text class="note" x="423" y="1130">Advice on</text>
        <text class="note" x="423" y="1143">structuring and</text>
        <text class="note" x="423" y="1156">management</text>

        <rect class="tab" x="244" y="1053" width="16" height="38"/>
        <text class="note note-right" x="238" y="1065">Optimize the return</text>
        <text class="note note-right" x="238" y="1078">on your after tax</text>
        <text class="note note-right" x="238" y="1091">income</text>

        <rect class="tab" x="189" y="898" width="16" height="38"/>
        <text class="note note-right" x="183" y="910">Protect the lifestyle</text>
        <text class="note note-right" x="183" y="923">you’ve built for you</text>
        <text class="note note-right" x="183" y="936">and your family</text>

        <rect class="tab" x="239" y="762" width="16" height="38"/>
        <text class="note note-right" x="233" y="774">Ensure your assets</text>
        <text class="note note-right" x="233" y="787">are dealt with as</text>
        <text class="note note-right" x="233" y="800">you want</text>
      </g>
    </g>

    <rect class="dark-band" x="19" y="1184" width="782" height="27"/>
    <text class="footer-text" x="386" y="1201" text-anchor="end">www.larkmoorcapital.com.au</text>
    <rect class="band-mark" x="403" y="1190" width="14" height="14"/>
    <text class="footer-text" x="434" y="1201">info@larkmoorcapital.com.au</text>
  </g>
</svg>
</body>
</html>
```